public page kestrel AX (www.kestrelax.com)

https://www.plumaquill.com/shard/s418/sh/b2190ce7-5d3a-4f1e-8c2b-6e7a1d94c0f2/47b1e9c2d0a83f56e1c7b9a2f4d60e81

compatible with wordpress

Designs look the same

Industry/Entity Type

Finance And Accounting

Coding

Coded - Design and coding required

Number of Pages Required

1 page

Font styles to use
Sans Serif

Colors
85cae6
3176b5
cfdeed
fac994
fff3d1
fefdec
cfcfcf
e8e8e8
9d9d9d

```html
<!DOCTYPE html>
<html lang="en">
<head>
<meta charset="utf-8">
<title>kestrel AX — Profit calculator for Marketra sellers</title>
<link rel="stylesheet" href="https://fonts.googleapis.com/css2?family=Montserrat:wght@500;600;700&family=Open+Sans:wght@400;600;700&display=swap">
<style>
  :root{
    --sky:#cfdeed;
    --cream:#fff3d1;
    --frame:#e8e8e8;
    --blue:#3176b5;
    --aqua:#85cae6;
    --peach:#fac994;
    --salmon:#f39a7b;
    --violet:#4f4f9e;
    --ink:#3d3d3d;
    --muted:#6f6f6f;
    --line:#cfcfcf;
    --grey:#9d9d9d;
    --white:#ffffff;
    --paper:#fefdec;
  }
  *{box-sizing:border-box;margin:0;padding:0}
  html,body{width:1200px;height:4196px;overflow:hidden}
  body{background:var(--frame);font-family:"Open Sans",Arial,sans-serif;color:var(--ink);position:relative}
  .page{position:absolute;left:14px;top:0;width:1172px;height:4182px;background:var(--cream);overflow:hidden}
  .abs{position:absolute}

  /* hero */
  .hero{left:0;top:0;width:1172px;height:1337px;background:var(--sky)}
  .brand{left:26px;top:28px;width:210px;text-align:center}
  .brand-mark{width:84px;height:84px;border-radius:50%;background:var(--blue);margin:0 auto 10px}
  .brand-name{font-family:"Open Sans",Arial,sans-serif;font-weight:600;font-size:27px;color:var(--blue);letter-spacing:1px}
  .nav{right:26px;top:42px;display:flex;align-items:center;gap:26px;font-family:"Montserrat",Arial,sans-serif;font-size:13px;font-weight:600;color:#2c3e5a;text-transform:uppercase}
  .nav .faq{text-transform:none}
  .nav .signup{border:2px solid var(--blue);color:var(--blue);border-radius:20px;padding:6px 16px}
  .nav .signin{background:var(--peach);border-radius:20px;padding:8px 18px;color:#2c3e5a}
  .nav .menu{width:36px;height:36px;border-radius:5px;background:#2f5d95;display:flex;flex-direction:column;justify-content:center;align-items:center;gap:4px;margin-left:-4px}
  .nav .menu span{display:block;width:16px;height:2px;background:var(--white)}
  .hero-art{left:20px;top:140px;width:500px;height:560px;border-radius:40px;background:radial-gradient(circle at 55% 40%,#f3c08a 0,#e9e9ef 38%,rgba(207,222,237,0) 70%)}
  .hero-title{left:613px;top:236px;width:550px;font-size:35px;line-height:45px;color:var(--blue);font-weight:400}
  .signup-form{left:607px;top:415px;display:flex;gap:8px}
  .signup-form .field{width:300px;height:48px;border-radius:24px;background:var(--white);font-size:16px;color:var(--grey);padding:14px 24px}
  .signup-form .go{width:208px;height:48px;border-radius:24px;background:var(--blue);color:var(--white);font-weight:600;font-size:16px;text-align:center;line-height:48px}
  .watch{left:778px;top:542px;display:flex;align-items:center;gap:12px;font-family:"Montserrat",Arial,sans-serif;font-weight:700;font-size:17px;color:#2c3e5a}
  .intro-title{left:0;top:812px;width:1172px;text-align:center;font-size:38px;line-height:46px;color:var(--violet);font-weight:400}
  .intro-copy{left:110px;top:955px;width:952px;text-align:center;font-size:17.5px;line-height:26px;color:var(--muted)}
  .intro-copy b{color:#555}
  .partners{left:78px;top:1097px;display:flex;gap:36px}
  .partner{width:227px;height:131px;background:var(--white);border-radius:4px;box-shadow:0 3px 10px rgba(40,60,90,.18);display:flex;align-items:center;justify-content:center}
  .partner i{display:block;width:120px;height:26px;border-radius:13px;background:var(--line)}

  /* features */
  .feature-art{border-radius:30px}
  .feature h2{font-size:40px;font-weight:400;color:var(--blue);line-height:48px;margin-bottom:14px}
  .feature p{font-size:18px;line-height:25px;color:var(--muted)}
  .f1{left:129px;top:1522px;width:520px}
  .f2{left:658px;top:1938px;width:470px}
  .f3{left:129px;top:2355px;width:480px}
  .f4{left:683px;top:2775px;width:440px}
  .a1{left:708px;top:1440px;width:350px;height:336px;background:radial-gradient(circle,#9fc6dc 0,#f5d7b8 45%,rgba(255,243,209,0) 72%)}
  .a2{left:196px;top:1818px;width:420px;height:294px;background:linear-gradient(160deg,#85cae6,#3a5a8c 60%,#cfdeed)}
  .a3{left:699px;top:2280px;width:364px;height:350px;background:linear-gradient(150deg,#cfdeed,#3b6f8f 55%,#2f5f7a)}
  .a4{left:126px;top:2700px;width:476px;height:321px;background:linear-gradient(135deg,#3a3f4a 0,#e86b58 45%,#fac994 80%)}

  .perks{left:0;top:3210px;width:1172px;display:flex;justify-content:space-around;padding:0 120px}
  .perk{width:300px;text-align:center}
  .perk svg{display:block;margin:0 auto 18px}
  .perk h3{font-size:18px;font-weight:600;color:var(--blue);margin-bottom:6px}
  .perk p{font-size:18px;line-height:25px;color:var(--muted)}

  .pricing{left:0;top:3552px;width:1172px;text-align:center}
  .pricing h2{font-size:50px;font-weight:400;color:var(--salmon);line-height:60px}
  .pricing .price{font-size:50px;font-weight:700;color:var(--salmon);line-height:60px}
  .pricing .cta{display:inline-block;margin-top:20px;width:204px;height:44px;line-height:44px;border-radius:22px;background:var(--peach);color:var(--white);font-size:15px;font-weight:600}

  /* footer */
  .foot-brand{left:84px;top:3860px;width:210px;text-align:center}
  .socials{left:96px;top:4032px;display:flex;gap:14px}
  .socials span{width:30px;height:30px;border-radius:50%;background:var(--blue)}
  .foot-col h4{font-size:18px;font-weight:700;color:var(--blue);margin-bottom:30px}
  .links{display:grid;grid-template-columns:151px 210px;row-gap:4px;font-size:18px;color:var(--muted);line-height:24px;white-space:nowrap}
  .quick{left:417px;top:3866px}
  .contact{left:878px;top:3866px}
  .contact li{list-style:none;display:flex;align-items:center;gap:10px;font-size:18px;color:var(--muted);margin-bottom:34px}
  .copyright{left:0;top:4145px;width:1172px;text-align:center;font-family:"Montserrat",Arial,sans-serif;font-size:11px;font-weight:600;color:#555;letter-spacing:.3px}
</style>
</head>
<body>
<div class="page">

  <section class="abs hero">
    <div class="abs hero-art" role="img" aria-label="Illustration of a businessman riding a rocket above clouds with money, chart and globe icons"></div>
    <div class="abs brand">
      <div class="brand-mark"></div>
      <div class="brand-name">KESTREL AX</div>
    </div>
    <nav class="abs nav">
      <span>• Home</span><span>Pricing</span><span>About</span><span>Contact</span><span>Blog</span><span class="faq">FAQs</span>
      <span class="signup">Sign up</span><span class="signin">Sign in</span>
      <span class="menu"><span></span><span></span><span></span></span>
    </nav>
    <h1 class="abs hero-title">We are building a simple and intuitive service for Marketra sellers to calculate their profit.</h1>
    <div class="abs signup-form">
      <div class="field">Your Email Address</div>
      <div class="go">Get Started</div>
    </div>
    <div class="abs watch">
      <svg width="24" height="24" viewBox="0 0 24 24"><circle cx="12" cy="12" r="10" fill="none" stroke="#2c3e5a" stroke-width="2"/><path d="M10 8l6 4-6 4z" fill="#2c3e5a"/></svg>
      WATCH VIDEO
    </div>
    <h2 class="abs intro-title">Profit is not something to add on at the end,<br>it is something to plan for in the beginning</h2>
    <p class="abs intro-copy"><b>KESTREL AX</b> is the first ever software created by <b>Real Needs</b> of the <b>Real Marketra Sellers</b> in cooperation with group of brilliant software engineers to help you manage your business and calculate your <b>Real Profit</b> on everyday basis.</p>
    <div class="abs partners">
      <div class="partner"><i></i></div>
      <div class="partner"><i></i></div>
      <div class="partner"><i></i></div>
      <div class="partner"><i></i></div>
    </div>
  </section>

  <div class="abs feature-art a1" role="img" aria-label="Illustration of a hand holding a magnifying glass surrounded by marketing icons"></div>
  <article class="abs feature f1">
    <h2>Find new keywords</h2>
    <p>Lorem ipsum dolor sit amet, consectetur adipiscing elit, sed do eiusmod tempor incididunt ut labore et do lore magna aliqua. Ut enim ad minim veniam, quis nos trud exercitation ullamco laboris nisi ut aliquip.</p>
  </article>

  <div class="abs feature-art a2" role="img" aria-label="Illustration of a team celebrating with dollar signs, a banner and a piggy bank"></div>
  <article class="abs feature f2">
    <h2>Boost your sales</h2>
    <p>Lorem ipsum dolor sit amet, consectetur adipiscing elit, sed do eiusmod tempor incididunt ut labore et dolore magna all qua ut enim ad minim veniam.</p>
  </article>

  <article class="abs feature f3">
    <h2>Automate PPC Campaign</h2>
    <p>Lorem ipsum dolor sit amet, consectetur adipis cing elit, sed do eiusmod tempor incididunt ut la bore et dolore magna aliqua. Ut enim ad minim veniam, quis nos trud exercitation.</p>
  </article>
  <div class="abs feature-art a3" role="img" aria-label="Illustration of a hand on a laptop keyboard with browser windows rising from the screen"></div>

  <div class="abs feature-art a4" role="img" aria-label="Illustration of a laptop showing a rocket launch and a hand holding a phone with a buy button"></div>
  <article class="abs feature f4">
    <h2>Success and make profit on Marketra</h2>
    <p>Lorem ipsum dolor sit amet, consecte tur adipiscing elit, sed do eiusmod tempor incididu ut labore et dolore magna aliqua.</p>
  </article>

  <section class="abs perks">
    <div class="perk">
      <svg width="76" height="62" viewBox="0 0 76 62" fill="none" stroke="#f08a6c" stroke-width="3"><rect x="6" y="36" width="10" height="22"/><rect x="22" y="28" width="10" height="30"/><rect x="38" y="32" width="10" height="26"/><rect x="54" y="20" width="10" height="38"/><path d="M8 24l18-10 14 6 24-16"/><path d="M56 4h8v8"/></svg>
      <h3>Complete Data Analytics</h3>
      <p>Lorem ipsum dolor sit amet, consectetur adipiscing elit, sed do eiusmod tempor inci didu ut labore et dolore.</p>
    </div>
    <div class="perk">
      <svg width="66" height="62" viewBox="0 0 66 62" fill="none" stroke="#f08a6c" stroke-width="3"><rect x="6" y="10" width="54" height="46" rx="4"/><path d="M6 20h54"/><circle cx="33" cy="38" r="9"/><path d="M33 35v6"/></svg>
      <h3>Security and Privacy</h3>
      <p>Lorem ipsum dolor sit amet, consectetur adipiscing elit, sed do eiusmod tempor inci didu ut labore et dolore.</p>
    </div>
    <div class="perk">
      <svg width="62" height="62" viewBox="0 0 62 62" fill="none" stroke="#f08a6c" stroke-width="3"><circle cx="31" cy="28" r="16"/><path d="M12 30v-4a19 19 0 0 1 38 0v4"/><rect x="8" y="26" width="7" height="12" rx="3"/><rect x="47" y="26" width="7" height="12" rx="3"/><path d="M14 58c3-8 10-12 17-12s14 4 17 12"/></svg>
      <h3>Expert Support</h3>
      <p>Lorem ipsum dolor sit amet, consectetur adipiscing elit, sed do eiusmod tempor inci didu ut labore et dolore.</p>
    </div>
  </section>

  <section class="abs pricing">
    <h2>Complete analytics solutions only</h2>
    <div class="price">$2.95/month*</div>
    <span class="cta">Get Started</span>
  </section>

  <footer>
    <div class="abs foot-brand">
      <div class="brand-mark"></div>
      <div class="brand-name">KESTREL AX</div>
    </div>
    <div class="abs socials"><span></span><span></span><span></span><span></span></div>
    <div class="abs foot-col quick">
      <h4>Quick Links</h4>
      <div class="links">
        <span>Home</span><span>FAQs</span>
        <span>Pricing</span><span>Sign Up</span>
        <span>About Us</span><span>Sign In</span>
        <span>Contact</span><span>Privacy Policy</span>
        <span>Blog</span><span>Terms &amp; Conditions</span>
      </div>
    </div>
    <div class="abs foot-col contact">
      <h4>Contact</h4>
      <ul>
        <li><svg width="20" height="20" viewBox="0 0 20 20" fill="none" stroke="#555" stroke-width="1.6"><circle cx="10" cy="10" r="8.5"/><path d="M7 5.5l2 2.5-1 1.2a6 6 0 0 0 2.8 2.8l1.2-1 2.5 2-1 1.5c-4 0-8-4-8-8z"/></svg>+1 555-014-2287</li>
        <li><svg width="20" height="20" viewBox="0 0 20 20" fill="none" stroke="#555" stroke-width="1.6"><circle cx="10" cy="10" r="8.5"/><path d="M5.5 7h9v6h-9z M5.5 7l4.5 3.5L14.5 7"/></svg>info@kestrelax.com</li>
      </ul>
    </div>
    <p class="abs copyright">COPYRIGHT © 2018 KESTRELAX. ALL RIGHTS RESERVED.</p>
  </footer>

</div>
</body>
</html>
```